Business Cards, Letter Heads and a4 size envolpes
Brantwick Holdings
Business Cards, Letter Heads and a4 size envolpes - Financial Services
Creative Brief
Simple
Jad K. Lorenby
Managing Partner
T : +971 4 3867041 M : +971 50 6183024(Ae) M: +255 773 482615 (Tz) P.O. Box 6174 Dubai UAE
jad@brantwickholdings-example.com
www.brantwickholdings-example.com

```html
<!DOCTYPE html>
<html lang="en">
<head>
<meta charset="utf-8">
<title>Brantwick Holdings – Business Card</title>
<link rel="stylesheet" href="https://fonts.googleapis.com/css2?family=Open+Sans:wght@300;400;600&display=swap">
<style>
  :root {
    --backdrop: #d9d9d9;
    --card: #050505;
    --band: #8f8d90;
    --ink: #ffffff;
    --ink-soft: #c9c9c9;
    --rule: #e6e6e6;
  }
  * { box-sizing: border-box; margin: 0; padding: 0; }
  html, body { width: 1200px; height: 897px; overflow: hidden; }
  body {
    background: var(--backdrop);
    font-family: "Open Sans", Arial, sans-serif;
    position: relative;
  }
  .card {
    position: absolute;
    left: 260px;
    width: 680px;
    height: 388px;
    background: var(--card);
    color: var(--ink);
    box-shadow: 0 6px 18px rgba(0,0,0,0.25);
  }
  .card--back { top: 36px; }
  .card--front { top: 472px; }

  .brand {
    position: absolute;
    left: 0; right: 0;
    display: flex;
    flex-direction: column;
    align-items: center;
    gap: 12px;
  }
  .card--back .brand { top: 105px; }
  .card--front .brand { top: 56px; }
  .brand__mark {
    width: 46px; height: 46px;
    border: 2px solid var(--ink);
    border-radius: 50%;
  }
  .brand__name {
    font-weight: 300;
    font-size: 34px;
    letter-spacing: 1px;
    color: var(--ink);
  }
  .card--front .brand__name { font-size: 30px; }

  .web-line {
    position: absolute;
    top: 250px; left: 0; right: 0;
    text-align: center;
    font-size: 11px;
    letter-spacing: 1.5px;
    color: var(--ink-soft);
  }

  .name-band {
    position: absolute;
    left: 0; right: 0;
    top: 196px;
    height: 38px;
    background: var(--band);
    border-top: 2px solid var(--rule);
    border-bottom: 2px solid var(--rule);
    box-shadow: 0 -6px 0 var(--card), 0 6px 0 var(--card), 0 -8px 0 var(--rule), 0 8px 0 var(--rule);
    display: flex;
    align-items: center;
    justify-content: center;
    gap: 8px;
    font-size: 14px;
    color: #1b1b1b;
  }
  .name-band__name { font-weight: 600; }
  .name-band__role { font-weight: 400; color: #2e2e2e; }

  .contacts {
    position: absolute;
    left: 28px; right: 20px;
    top: 268px;
    display: grid;
    grid-template-columns: 1fr 1fr 1fr;
    row-gap: 22px;
    column-gap: 10px;
    font-size: 11.5px;
    color: var(--ink-soft);
  }
  .contact { display: flex; align-items: center; gap: 7px; white-space: nowrap; }
  .contact__icon { width: 16px; height: 16px; flex: none; }
</style>
</head>
<body>

  <section class="card card--back" aria-label="Business card, back">
    <div class="brand">
      <span class="brand__mark"></span>
      <span class="brand__name">Brantwick Holdings</span>
    </div>
    <p class="web-line">www.brantwickholdings-example.com</p>
  </section>

  <section class="card card--front" aria-label="Business card, front">
    <div class="brand">
      <span class="brand__mark"></span>
      <span class="brand__name">Brantwick Holdings</span>
    </div>

    <div class="name-band">
      <span class="name-band__name">Jad K. Lorenby</span>
      <span class="name-band__role">| Managing Partner</span>
    </div>

    <div class="contacts">
      <div class="contact">
        <svg class="contact__icon" viewBox="0 0 16 16"><circle cx="8" cy="8" r="8" fill="#bdbdbd"/><path d="M8 3.5a2.6 2.6 0 0 0-2.6 2.6C5.4 8.2 8 12 8 12s2.6-3.8 2.6-5.9A2.6 2.6 0 0 0 8 3.5z" fill="#050505"/><circle cx="8" cy="6.1" r="0.9" fill="#bdbdbd"/></svg>
        <span>P.O. Box 6174 Dubai UAE</span>
      </div>
      <div class="contact">
        <svg class="contact__icon" viewBox="0 0 16 16"><circle cx="8" cy="8" r="8" fill="#bdbdbd"/><path d="M5.2 4.2l1.4-.4 1 2-.9.8c.4 1 1.1 1.7 2.1 2.1l.8-.9 2 1-.4 1.4c-3.2.2-6.1-2.8-6-6z" fill="#050505"/></svg>
        <span>+971 4 3867041</span>
      </div>
      <div class="contact">
        <svg class="contact__icon" viewBox="0 0 16 16"><circle cx="8" cy="8" r="8" fill="#bdbdbd"/><rect x="5.6" y="3.4" width="4.8" height="9.2" rx="0.8" fill="#050505"/><rect x="6.4" y="4.5" width="3.2" height="6" fill="#bdbdbd"/></svg>
        <span>+971 50 6183024(Ae)</span>
      </div>
      <div class="contact">
        <svg class="contact__icon" viewBox="0 0 16 16"><circle cx="8" cy="8" r="8" fill="#bdbdbd"/><rect x="5.6" y="3.4" width="4.8" height="9.2" rx="0.8" fill="#050505"/><rect x="6.4" y="4.5" width="3.2" height="6" fill="#bdbdbd"/></svg>
        <span>+255 773 482615 (Tz)</span>
      </div>
      <div class="contact">
        <svg class="contact__icon" viewBox="0 0 16 16"><circle cx="8" cy="8" r="8" fill="#bdbdbd"/><rect x="4" y="5" width="8" height="6" fill="#050505"/><path d="M4.3 5.3L8 8.3l3.7-3" stroke="#bdbdbd" stroke-width="0.8" fill="none"/></svg>
        <span>jad@brantwickholdings-example.com</span>
      </div>
      <div class="contact">
        <svg class="contact__icon" viewBox="0 0 16 16"><circle cx="8" cy="8" r="8" fill="#bdbdbd"/><circle cx="8" cy="8" r="4" fill="none" stroke="#050505" stroke-width="1"/><path d="M4 8h8M8 4c-2 2.4-2 5.6 0 8M8 4c2 2.4 2 5.6 0 8" stroke="#050505" stroke-width="0.8" fill="none"/></svg>
        <span>www.brantwickholdings-example.com</span>
      </div>
    </div>
  </section>

</body>
</html>
```